Whitmore Business Card Design

The name of the business is Dara Whitmore, CPA LLC
The service that we offer is Accounting, Tax & Consulting Services. I need it to have the following items:
Dara Whitmore, Principal
Phone Number
Email Address
Physical Address

I have attached the company logo, one in black and one in white. Please provide a design in black background and the other in white background. Please include "Accounting, Tax & Consulting Services". I want the business card to be clean and very professional.

```html
<!DOCTYPE html>
<html lang="en">
<head>
<meta charset="utf-8">
<title>Dara Whitmore, CPA LLC — Business Card</title>
<link rel="stylesheet" href="https://fonts.googleapis.com/css2?family=Montserrat:ital,wght@0,400;0,500;0,600;0,700;1,400&display=swap">
<style>
  :root {
    --stage: #d8d8da;
    --card: #231f20;
    --red: #9e1c20;
    --red-bright: #b5222a;
    --grey: #9d9d9f;
    --grey-light: #c9c9cb;
    --text-soft: #d2d2d2;
    --rule: #6e6e70;
  }
  * { margin: 0; padding: 0; box-sizing: border-box; }
  html, body { width: 1200px; height: 1000px; overflow: hidden; }
  body {
    background: var(--stage);
    font-family: "Montserrat", Arial, sans-serif;
    position: relative;
  }
  .card {
    position: absolute;
    width: 692px;
    height: 384px;
    background: var(--card);
    overflow: hidden;
  }
  .card--front { left: 124px; top: 82px; }
  .card--back { left: 336px; top: 492px; }

  /* Front */
  .accent-bar {
    position: absolute; left: 62px; top: 0;
    width: 32px; height: 133px; background: var(--red);
  }
  .holder-name {
    position: absolute; left: 106px; top: 90px;
    font-size: 24px; font-weight: 500; letter-spacing: 0.5px;
    color: var(--grey);
  }
  .holder-name strong { font-weight: 700; }
  .holder-title {
    position: absolute; left: 106px; top: 121px;
    font-size: 11.5px; font-style: italic; letter-spacing: 1.5px;
    color: var(--grey);
  }
  .title-rule {
    position: absolute; left: 194px; top: 128px;
    width: 154px; height: 2px; background: var(--grey);
  }
  .title-rule::after {
    content: ""; position: absolute; right: 0; top: -0.5px;
    width: 42px; height: 3px; background: var(--grey-light);
  }
  .divider {
    position: absolute; left: 83px; top: 173px;
    width: 525px; height: 5px;
  }
  .divider .red { position: absolute; left: 0; top: 1px; width: 348px; height: 2px; background: var(--red-bright); }
  .divider .grey { position: absolute; left: 348px; top: 0; width: 177px; height: 5px; background: var(--grey); }

  .contact-list { list-style: none; }
  .contact {
    position: absolute; left: 79px;
    width: 233px; height: 32px;
    border-bottom: 1px solid var(--rule);
  }
  .contact--phone { top: 189px; }
  .contact--email { top: 240px; }
  .contact--address { top: 290px; }
  .contact-icon {
    position: absolute; left: 0; top: 0;
    width: 32px; height: 32px;
    background: var(--grey-light);
    border-radius: 8px 14px 0 8px;
    display: flex; align-items: center; justify-content: center;
  }
  .contact-icon svg { width: 18px; height: 18px; }
  .contact-text {
    position: absolute; left: 43px; top: 8px;
    font-size: 12.5px; letter-spacing: 1px; color: var(--text-soft);
  }

  .firm-mark {
    position: absolute; left: 354px; top: 256px;
    display: flex; align-items: center; gap: 10px;
  }
  .firm-mark .mark-square { width: 30px; height: 30px; background: var(--grey); flex: none; }
  .firm-mark .firm-name {
    font-size: 14px; font-weight: 600; letter-spacing: 0.4px;
    color: var(--grey); line-height: 1.15; text-transform: uppercase;
  }
  .firm-mark .firm-sub {
    display: block; font-size: 11px; font-weight: 600; letter-spacing: 0.8px;
    color: var(--grey-light); text-transform: uppercase;
  }
  .front-band {
    position: absolute; left: 0; bottom: 0;
    width: 100%; height: 16px; background: var(--grey);
  }

  /* Back */
  .back-rule {
    position: absolute; left: 138px; width: 416px; height: 2px;
  }
  .back-rule--top { top: 115px; background: var(--grey); }
  .back-rule--bottom { top: 266px; background: var(--red-bright); }
  .back-mark {
    position: absolute; left: 138px; top: 148px;
    width: 416px;
    display: flex; align-items: center; gap: 16px;
  }
  .back-mark .mark-square { width: 52px; height: 52px; background: var(--grey); flex: none; }
  .back-mark .firm-name {
    font-size: 21px; font-weight: 600; letter-spacing: 0.6px;
    color: var(--grey); text-transform: uppercase; line-height: 1.2;
  }
  .back-mark .firm-sub {
    display: block; font-size: 17px; font-weight: 600; letter-spacing: 1px;
    color: var(--grey-light); text-transform: uppercase;
  }
  .services {
    position: absolute; left: 138px; top: 217px;
    width: 416px; text-align: center;
    font-size: 18.5px; font-weight: 600; letter-spacing: 0.3px;
    color: var(--grey);
  }
  .back-band {
    position: absolute; left: 0; bottom: 0;
    width: 100%; height: 16px; background: var(--red);
  }
</style>
</head>
<body>

<section class="card card--front" aria-label="Business card front">
  <div class="accent-bar"></div>
  <h1 class="holder-name"><strong>DARA</strong> WHITMORE</h1>
  <p class="holder-title">PRINCIPAL</p>
  <div class="title-rule"></div>
  <div class="divider"><span class="red"></span><span class="grey"></span></div>

  <ul class="contact-list">
    <li class="contact contact--phone">
      <span class="contact-icon">
        <svg viewBox="0 0 24 24" fill="none" stroke="#9e1c20" stroke-width="2" stroke-linecap="round" stroke-linejoin="round"><path d="M5 3h4l2 5-2.5 1.5a11 11 0 0 0 6 6L16 13l5 2v4a2 2 0 0 1-2 2A17 17 0 0 1 3 5a2 2 0 0 1 2-2z"/></svg>
      </span>
      <span class="contact-text">+111 555 0199</span>
    </li>
    <li class="contact contact--email">
      <span class="contact-icon">
        <svg viewBox="0 0 24 24" fill="none" stroke="#9e1c20" stroke-width="2"><circle cx="12" cy="12" r="9"/><path d="M3 12h18M12 3c3 3.5 3 14.5 0 18M12 3c-3 3.5-3 14.5 0 18"/></svg>
      </span>
      <span class="contact-text">info@darawhitmore.com</span>
    </li>
    <li class="contact contact--address">
      <span class="contact-icon">
        <svg viewBox="0 0 24 24"><path d="M12 2a7 7 0 0 0-7 7c0 5 7 12 7 12s7-7 7-12a7 7 0 0 0-7-7z" fill="#9e1c20"/><circle cx="12" cy="9" r="2.5" fill="#c9c9cb"/></svg>
      </span>
      <span class="contact-text">Your Address Here 00123</span>
    </li>
  </ul>

  <div class="firm-mark">
    <span class="mark-square"></span>
    <span class="firm-name">Dara Whitmore, CPA LLC
      <span class="firm-sub">Certified Public Accountant</span>
    </span>
  </div>
  <div class="front-band"></div>
</section>

<section class="card card--back" aria-label="Business card back">
  <div class="back-rule back-rule--top"></div>
  <div class="back-mark">
    <span class="mark-square"></span>
    <span class="firm-name">Dara Whitmore, CPA LLC
      <span class="firm-sub">Certified Public Accountant</span>
    </span>
  </div>
  <p class="services">Accounting, Tax &amp; Consulting Services</p>
  <div class="back-rule back-rule--bottom"></div>
  <div class="back-band"></div>
</section>

</body>
</html>
```